8 1/2 x 11 Flyer Design for Water Damage Restoration Company

Houston Texas based Water Damage Restoration company is needing a advertising flyer that highlights water damage and water extraction.

KESTRAL Emergency Services
52710 Harlow Crossing Suite G4
Houston, Texas 77193
713-846-5170
www.KESTRAL58129.example

Water Damage Restoration
Water Extraction
Mold Prevention
24/7/365
FREE Evaluations

Suggested photos to use:
Water Damage
Leaking Pipes
Water on floors and ground
Water pouring from ceilings
Technicians
Company Logo
Photos

Company Colors:
Orange and Blue

```html
<!DOCTYPE html>
<html lang="en">
<head>
<meta charset="utf-8">
<title>KESTRAL Emergency Services Flyer</title>
<link href="https://fonts.googleapis.com/css2?family=Montserrat:wght@800;900&family=Hind:wght@500;600;700&family=Oswald:wght@600&display=swap" rel="stylesheet">
<style>
  :root {
    --navy: #1d3a72;
    --orange: #f26a1b;
    --white: #ffffff;
    --page: #29313b;
    --sky-light: #dcebfb;
    --sky-deep: #84bcf2;
    --water: #3b86d6;
  }
  * { margin: 0; padding: 0; box-sizing: border-box; }
  html, body { width: 1200px; height: 2646px; overflow: hidden; background: var(--page); }
  .flyer {
    position: absolute; left: 146px; top: 1240px;
    width: 910px; height: 1175px;
    background: var(--white); overflow: hidden;
    font-family: "Hind", sans-serif; color: var(--navy);
  }
  .hero-photo {
    position: absolute; left: 0; top: 0; width: 910px; height: 620px;
    background:
      radial-gradient(ellipse at 30% 20%, #c9cfd6 0%, rgba(201,207,214,0) 55%),
      radial-gradient(ellipse at 85% 15%, #b9bec4 0%, rgba(185,190,196,0) 50%),
      linear-gradient(180deg, #aac6df 0%, #c4c7cb 30%, #6f5a4c 55%, #7b3f2e 75%, #5b3a2e 100%);
  }
  .shapes { position: absolute; left: 0; top: 0; width: 910px; height: 1175px; }
  .photo-circle {
    position: absolute; border-radius: 50%; border: 9px solid var(--white);
    box-shadow: 0 4px 14px rgba(0,0,0,.25);
  }
  .photo-circle.storm { left: 227px; top: 403px; width: 222px; height: 222px;
    background: linear-gradient(160deg, #9fb6c9 0%, #6b6a4e 45%, #d9cc8e 75%, #8a8370 100%); }
  .photo-circle.leak { left: 557px; top: 245px; width: 268px; height: 268px;
    background: linear-gradient(135deg, #e9ecef 0%, #c9ced3 45%, #3f8fd6 70%, #1b4fc4 100%); }
  .brand {
    position: absolute; left: 0; width: 910px; top: 70px; text-align: center;
    font-family: "Montserrat", sans-serif; font-weight: 900; color: var(--navy);
    font-size: 50px; line-height: 1.05; letter-spacing: -0.5px;
  }
  .brand .mark { display: inline-block; width: 26px; height: 26px; border-radius: 50%;
    background: var(--navy); margin-right: 12px; vertical-align: 6px; }
  .brand small { display: block; font-size: 30px; }
  .tagline { position: absolute; left: 496px; top: 549px; width: 320px;
    font-weight: 700; font-size: 22px; line-height: 25px; }
  .services-title { position: absolute; left: 494px; top: 628px;
    font-family: "Oswald", sans-serif; font-weight: 600; font-size: 36px; color: var(--orange); }
  .services-rule { position: absolute; left: 494px; top: 678px; width: 305px; height: 2px; background: var(--navy); }
  .services { position: absolute; left: 496px; top: 694px; list-style: none;
    font-weight: 600; font-size: 21px; line-height: 31.4px; }
  .services li { display: flex; align-items: center; }
  .services svg { width: 13px; height: 13px; margin-right: 2px; }
  .headline { position: absolute; left: 97px; top: 628px;
    font-family: "Montserrat", sans-serif; font-weight: 900; line-height: 55px; font-size: 55px; }
  .headline .name { color: var(--navy); display: block; }
  .headline .accent { color: var(--orange); display: block; }
  .headline .promise { display: block; color: var(--navy); font-size: 27px; line-height: 28px;
    font-weight: 800; margin-top: 4px; width: 360px; }
  .specialty { position: absolute; display: flex; align-items: center; gap: 6px;
    font-family: "Hind", sans-serif; font-weight: 700; font-size: 25px; color: var(--navy); }
  .specialty svg { width: 40px; height: 40px; }
  .specialty.water { left: 95px; top: 906px; }
  .specialty.fire { left: 297px; top: 906px; }
  .specialty.contents { left: 95px; top: 970px; }
  .water-band { position: absolute; left: 0; top: 1040px; width: 910px; height: 135px; }
  .call-badge { position: absolute; left: 505px; top: 948px; width: 160px; height: 115px;
    transform: rotate(-8deg); z-index: 2; }
  .footer { position: absolute; left: 0; top: 1110px; width: 910px; height: 50px;
    font-weight: 600; font-size: 19px; color: var(--navy); }
  .footer .item { position: absolute; display: flex; align-items: center; gap: 6px; }
  .footer svg { width: 18px; height: 18px; }
  .footer .phone { left: 95px; top: 12px; }
  .footer .web { left: 305px; top: 12px; }
  .footer .address { left: 600px; top: 2px; font-size: 15px; line-height: 16px; }
</style>
</head>
<body>
<main class="flyer">
  <div class="hero-photo" role="img" aria-label="Photo of a brick house with smoke rising from its roof under a cloudy sky"></div>

  <svg class="shapes" viewBox="0 0 910 1175" aria-hidden="true">
    <path d="M340 555 C400 490 460 470 540 485 C640 500 760 450 910 300 L910 390 C760 480 640 520 540 510 C470 500 420 490 360 540 Z" fill="var(--orange)"/>
    <path d="M0 445 C70 435 130 530 190 590 C240 630 300 590 360 540 C420 490 470 500 540 510 C640 520 760 480 910 390 L910 1175 L0 1175 Z" fill="var(--white)"/>
  </svg>

  <div class="photo-circle storm" role="img" aria-label="Photo of a fallen tree resting on a house roof"></div>
  <div class="photo-circle leak" role="img" aria-label="Photo of a woman on the phone holding a bucket under a leaking ceiling"></div>

  <div class="brand"><span class="mark"></span>KESTRAL<small>Emergency Services</small></div>

  <p class="tagline">Water Damage, Floods, Fire, Smoke, Mold Prevention, Contents Specialists</p>
  <h2 class="services-title">OUR SERVICES</h2>
  <div class="services-rule"></div>
  <ul class="services">
    <li><svg viewBox="0 0 12 12"><path d="M1 6 L4.5 10 L11 1" fill="none" stroke="#2e86d6" stroke-width="2"/></svg>24/7/365 Emergency Response</li>
    <li><svg viewBox="0 0 12 12"><path d="M1 6 L4.5 10 L11 1" fill="none" stroke="#2e86d6" stroke-width="2"/></svg>FREE Evaluations</li>
    <li><svg viewBox="0 0 12 12"><path d="M1 6 L4.5 10 L11 1" fill="none" stroke="#2e86d6" stroke-width="2"/></svg>A+ Rated Service Provider</li>
    <li><svg viewBox="0 0 12 12"><path d="M1 6 L4.5 10 L11 1" fill="none" stroke="#2e86d6" stroke-width="2"/></svg>Fully Insured</li>
    <li><svg viewBox="0 0 12 12"><path d="M1 6 L4.5 10 L11 1" fill="none" stroke="#2e86d6" stroke-width="2"/></svg>Certified Technicians</li>
    <li><svg viewBox="0 0 12 12"><path d="M1 6 L4.5 10 L11 1" fill="none" stroke="#2e86d6" stroke-width="2"/></svg>All Insurance Carriers</li>
    <li><svg viewBox="0 0 12 12"><path d="M1 6 L4.5 10 L11 1" fill="none" stroke="#2e86d6" stroke-width="2"/></svg>Direct Insurance Billing</li>
    <li><svg viewBox="0 0 12 12"><path d="M1 6 L4.5 10 L11 1" fill="none" stroke="#2e86d6" stroke-width="2"/></svg>Claimworks Invoices</li>
  </ul>

  <h1 class="headline">
    <span class="name">KESTRAL</span>
    <span class="accent">EMERGENCY</span>
    <span class="accent">SERVICES</span>
    <span class="promise">IS THERE WHEN YOUR CLIENTS NEED HELP THE MOST!</span>
  </h1>

  <div class="specialty water"><svg viewBox="0 0 40 40"><path d="M12 4 C6 13 4 17 4 21 a8 8 0 0 0 16 0 C20 17 18 13 12 4Z" fill="var(--navy)"/><path d="M26 16 C21 24 20 27 20 30 a6 6 0 0 0 12 0 C32 27 31 24 26 16Z" fill="none" stroke="var(--navy)" stroke-width="2"/><path d="M28 3v6M32 2v5M35 5v6" stroke="var(--navy)" stroke-width="2"/></svg>WATER</div>
  <div class="specialty fire"><svg viewBox="0 0 40 40"><path d="M20 2 C24 10 32 14 32 25 a12 12 0 0 1 -24 0 C8 18 12 14 14 10 C15 16 18 17 18 17 C17 10 18 6 20 2Z" fill="var(--navy)"/><path d="M20 22 C23 26 25 28 25 31 a5 5 0 0 1 -10 0 C15 28 18 25 20 22Z" fill="var(--white)"/></svg>FIRE</div>
  <div class="specialty contents"><svg viewBox="0 0 40 40"><path d="M3 12 L16 6 L29 12 L29 28 L16 34 L3 28 Z M3 12 L16 18 L29 12 M16 18 V34" fill="none" stroke="var(--navy)" stroke-width="3"/><circle cx="29" cy="27" r="6" fill="var(--white)" stroke="var(--navy)" stroke-width="3"/><path d="M33 31 L38 37" stroke="var(--navy)" stroke-width="3"/></svg>CONTENTS EXPERTS!</div>

  <svg class="water-band" viewBox="0 0 910 135" preserveAspectRatio="none" aria-hidden="true">
    <defs>
      <linearGradient id="sea" x1="0" y1="0" x2="0" y2="1">
        <stop offset="0" stop-color="#ffffff"/>
        <stop offset="0.45" stop-color="var(--sky-light)"/>
        <stop offset="1" stop-color="var(--sky-deep)"/>
      </linearGradient>
    </defs>
    <path d="M0 22 C120 10 240 30 380 20 C520 10 640 8 780 12 C840 14 880 6 910 2 L910 135 L0 135 Z" fill="url(#sea)"/>
    <path d="M0 18 C120 6 240 26 380 16 C520 6 640 4 780 8 C840 10 880 2 910 -2" fill="none" stroke="var(--orange)" stroke-width="2" opacity=".7"/>
    <path d="M0 24 C120 12 240 32 380 22 C520 12 640 10 780 14 C840 16 880 8 910 4" fill="none" stroke="var(--water)" stroke-width="4"/>
  </svg>

  <svg class="call-badge" viewBox="0 0 160 115" aria-label="Stop and call now, 24/7">
    <path d="M80 4 L156 58 L138 58 L138 112 L22 112 L22 58 L4 58 Z" fill="var(--navy)"/>
    <rect x="70" y="24" width="20" height="16" fill="var(--white)"/>
    <path d="M66 26 L80 14 L94 26" fill="none" stroke="var(--white)" stroke-width="3"/>
    <text x="80" y="60" text-anchor="middle" font-family="Hind, sans-serif" font-weight="700" font-size="11" fill="var(--white)">STOP &amp; CALL NOW!</text>
    <text x="80" y="100" text-anchor="middle" font-family="Montserrat, sans-serif" font-weight="900" font-size="38" fill="var(--white)">24/7</text>
  </svg>

  <footer class="footer">
    <span class="item phone"><svg viewBox="0 0 20 20"><path d="M4 2 L8 2 L9 7 L6.5 8.5 C8 11.5 9.5 13 12 14 L13.5 11.5 L18 12.5 L18 16 C18 17 17 18 16 18 C8 17 3 12 2 4 C2 3 3 2 4 2Z" fill="var(--navy)"/></svg>713-846-5170</span>
    <span class="item web"><svg viewBox="0 0 20 20"><circle cx="10" cy="10" r="8" fill="none" stroke="var(--navy)" stroke-width="2"/><ellipse cx="10" cy="10" rx="3.5" ry="8" fill="none" stroke="var(--navy)" stroke-width="1.5"/><path d="M2 10 H18" stroke="var(--navy)" stroke-width="1.5"/></svg>www.KESTRAL58129.example</span>
    <span class="item address"><svg viewBox="0 0 20 20"><path d="M10 1 a6 6 0 0 1 6 6 C16 12 10 19 10 19 C10 19 4 12 4 7 a6 6 0 0 1 6 -6Z" fill="var(--navy)"/><circle cx="10" cy="7" r="2.3" fill="var(--white)"/></svg><span>52710 Harlow Crossing Suite G4<br>Houston, Texas 77193</span></span>
  </footer>
</main>
</body>
</html>
```